BARRIER BANNER OTP

I am looking for a visual for a banner
3 meters long by 1 high.
In the same theme as the visual identity of the company.
As simple as possible without overloading

There must be the LOGO, the title TECHNIQUE SERVICES ROUSSEL

_________________________

I am looking for a visual for a banner (barrier banner)
3 meters long by 1 high.

AIR CONDITIONING HEATING VENTILATION
04 52 31 64 19

Font styles to use
Sans Serif

Colors
33b8a4
00a990
33a6d7
0493ce
3176b5
0355a3
ffffff

Requirements
Should not have
• No photo
No photo

```html
<!DOCTYPE html>
<html lang="en">
<head>
<meta charset="utf-8">
<title>OTP Barrier Banner</title>
<link rel="stylesheet" href="https://fonts.googleapis.com/css2?family=Montserrat:wght@500;600;700;800&display=swap">
<style>
  :root {
    --slate: #2f3a45;
    --green: #3ec985;
    --teal: #00a990;
    --teal-light: #33b8a4;
    --sky: #33a6d7;
    --blue: #0493ce;
    --blue-mid: #3176b5;
    --blue-deep: #0355a3;
    --white: #ffffff;
    --stage: #e4e6e8;
  }
  * { box-sizing: border-box; margin: 0; padding: 0; }
  html, body {
    width: 1200px; height: 516px; overflow: hidden;
    background: var(--stage);
    font-family: "Montserrat", sans-serif;
  }
  .banner {
    position: absolute; left: 0; top: 58px;
    width: 1200px; height: 400px;
    background: var(--slate);
    overflow: hidden;
  }
  .contact-band {
    position: absolute; left: 0; bottom: 0;
    width: 100%; height: 70px;
    background: var(--white);
  }
  .title {
    position: absolute; left: 56px; top: 22px;
    font-weight: 800; font-size: 56px; line-height: 53px;
    letter-spacing: 0.5px;
    color: var(--green);
  }
  .title span { display: block; }
  .title .title-last { color: var(--white); }
  .services {
    position: absolute; left: 56px; top: 206px;
  }
  .service {
    position: absolute; top: 0;
    display: flex; flex-direction: column; align-items: center;
    transform: translateX(-50%);
    white-space: nowrap;
  }
  .service svg { width: 60px; height: 68px; }
  .service-label {
    margin-top: 9px;
    font-weight: 600; font-size: 19.5px; color: var(--white);
  }
  .phone {
    position: absolute; left: 56px; top: 342px;
    font-size: 38px; line-height: 44px;
    white-space: nowrap;
  }
  .phone .call { color: var(--green); font-weight: 500; }
  .phone .number { color: var(--slate); font-weight: 700; margin-left: 14px; }
  .visuals {
    position: absolute; left: 0; top: 0;
    width: 1200px; height: 400px;
  }
  .logo-box {
    position: absolute; left: 1023px; top: 0;
    width: 146px; height: 96px;
    background: var(--white);
    border-radius: 0 0 9px 9px;
    display: flex; align-items: center; justify-content: center;
  }
  .logo-name {
    font-weight: 800; font-size: 46px; color: var(--slate);
    letter-spacing: 1px;
  }
</style>
</head>
<body>
  <div class="banner">
    <div class="contact-band"></div>

    <h1 class="title">
      <span>TECHNIQUE</span>
      <span>SERVICES</span>
      <span class="title-last">ROUSSEL</span>
    </h1>

    <svg width="0" height="0" style="position:absolute" aria-hidden="true">
      <defs>
        <linearGradient id="hexFill" x1="0" y1="0" x2="0" y2="1">
          <stop offset="0" stop-color="#33b8a4"/>
          <stop offset="1" stop-color="#0355a3"/>
        </linearGradient>
      </defs>
    </svg>

    <div class="services">
      <div class="service" style="left:91px">
        <svg viewBox="0 0 60 68" aria-hidden="true">
          <polygon points="30,2 57,17.5 57,50.5 30,66 3,50.5 3,17.5" fill="url(#hexFill)" stroke="#fff" stroke-width="2"/>
          <rect x="15" y="24" width="30" height="13" rx="2" fill="none" stroke="#fff" stroke-width="2"/>
          <line x1="19" y1="32" x2="41" y2="32" stroke="#fff" stroke-width="1.5"/>
          <path d="M30 12v9M26 14l8 5M34 14l-8 5" stroke="#fff" stroke-width="1.5"/>
          <path d="M24 41c-2 3 2 4 0 7M30 41c-2 3 2 4 0 7M36 41c-2 3 2 4 0 7" fill="none" stroke="#fff" stroke-width="1.5"/>
        </svg>
        <span class="service-label">AIR CONDITIONING</span>
      </div>
      <div class="service" style="left:259px">
        <svg viewBox="0 0 60 68" aria-hidden="true">
          <polygon points="30,2 57,17.5 57,50.5 30,66 3,50.5 3,17.5" fill="url(#hexFill)" stroke="#fff" stroke-width="2"/>
          <path d="M30 14c2 8 12 12 12 24a12 12 0 0 1-24 0c0-6 4-9 5-14 2 4 3 6 5 7 1-6-1-11 2-17z" fill="#fff"/>
          <path d="M30 34c3 4 6 6 6 10a6 6 0 0 1-12 0c0-4 3-6 6-10z" fill="#0f7d9a"/>
        </svg>
        <span class="service-label">HEATING</span>
      </div>
      <div class="service" style="left:397px">
        <svg viewBox="0 0 60 68" aria-hidden="true">
          <polygon points="30,2 57,17.5 57,50.5 30,66 3,50.5 3,17.5" fill="url(#hexFill)" stroke="#fff" stroke-width="2"/>
          <circle cx="30" cy="34" r="16" fill="none" stroke="#fff" stroke-width="2"/>
          <g fill="#fff">
            <path d="M30 34c-2-6-1-12 4-13s5 6-4 13z"/>
            <path d="M30 34c6-1 11 2 10 7s-7 3-10-7z"/>
            <path d="M30 34c-4 5-10 6-12 2s4-7 12-2z"/>
          </g>
          <circle cx="30" cy="34" r="3" fill="#0493ce" stroke="#fff" stroke-width="1.5"/>
        </svg>
        <span class="service-label">VENTILATION</span>
      </div>
    </div>

    <p class="phone"><span class="call">CALL</span><span class="number">04 52 31 64 19</span></p>

    <svg class="visuals" viewBox="0 0 1200 400" aria-hidden="true">
      <defs>
        <linearGradient id="panelWide" x1="0" y1="0" x2="1" y2="1">
          <stop offset="0" stop-color="#33a6d7"/>
          <stop offset="0.55" stop-color="#3176b5"/>
          <stop offset="1" stop-color="#0355a3"/>
        </linearGradient>
        <clipPath id="columnClip">
          <path d="M664,0 L779,0 Q698,200 773,400 L669,400 Q589.5,200 664,0 Z"/>
        </clipPath>
      </defs>

      <path d="M660,0 L1200,0 L1200,400 L665,400 Q585.5,200 660,0 Z" fill="var(--green)"/>

      <g clip-path="url(#columnClip)">
        <rect x="580" y="0" width="210" height="132" fill="var(--teal-light)"/>
        <rect x="580" y="136" width="210" height="128" fill="var(--blue)"/>
        <rect x="580" y="268" width="210" height="132" fill="var(--blue-mid)"/>
      </g>

      <path d="M787,0 L1200,0 L1200,400 L781,400 Q702,200 787,0 Z" fill="url(#panelWide)"/>
      <path d="M1200,230 Q1000,300 860,400 L1200,400 Z" fill="var(--blue-deep)" opacity="0.55"/>
      <path d="M1200,120 Q960,200 820,400 L860,400 Q1000,300 1200,230 Z" fill="var(--teal)" opacity="0.35"/>
    </svg>

    <div class="logo-box">
      <span class="logo-name">OTP</span>
    </div>
  </div>
</body>
</html>
```